Label for Refill packaging eco-conscious beauty brand

We need a label for our refill pouch. Velvet Harbor is an unscented conditioner formulated using the finest healthy & pure ingredients, free of chemicals and harmful toxins. As a minimalist beauty brand we are proud to be certified with TQB, Norvamark and Silver Kestrel.

We already have the pouches and an exciting label for our regular bottles.
We choose a kraft brown packing for the refill pouch and would like something minimalist but elegant for the label.

```html
<!DOCTYPE html>
<html lang="en">
<head>
<meta charset="utf-8">
<title>Velvet Harbor – Refill Pouch Labels</title>
<link href="https://fonts.googleapis.com/css2?family=Marcellus&family=Italiana&family=Josefin+Sans:wght@300&family=Montserrat:wght@400;500&display=swap" rel="stylesheet">
<style>
  :root {
    --backdrop: #25616e;
    --gold: #c9a64a;
    --gold-light: #ecd68a;
    --deep-panel: #375c6a;
    --deep-panel-dark: #2b4c59;
    --deep-band: #4b717e;
    --deep-text: #f1ede4;
    --mist-panel: #b4c0c1;
    --mist-band: #5d818b;
    --mist-text: #3e5e6a;
    --blush-panel: #e6d7cc;
    --blush-band: #8c7f83;
    --blush-text: #6e5f60;
  }
  * { box-sizing: border-box; margin: 0; padding: 0; }
  html, body { width: 1200px; height: 575px; overflow: hidden; }
  body {
    background: var(--backdrop);
    display: flex;
    align-items: center;
    justify-content: space-evenly;
    font-family: "Montserrat", sans-serif;
  }
  .label {
    width: 340px;
    height: 425px;
    display: flex;
    flex-direction: column;
    color: var(--ink);
  }
  .label--deep  { --panel: var(--deep-panel);  --band: var(--deep-band);  --ink: var(--deep-text); --sub: rgba(241,237,228,.75); }
  .label--mist  { --panel: var(--mist-panel);  --band: var(--mist-band);  --ink: var(--mist-text); --sub: rgba(62,94,106,.7); }
  .label--blush { --panel: var(--blush-panel); --band: var(--blush-band); --ink: var(--blush-text); --sub: rgba(110,95,96,.7); }
  .label--deep .label__panel { background: linear-gradient(160deg, #4a6f7c, var(--deep-panel) 45%, var(--deep-panel-dark)); }

  .label__leaf-band {
    height: 106px;
    background: linear-gradient(120deg, var(--band) 0%, var(--gold) 30%, var(--band) 45%, var(--band) 60%, var(--gold-light) 75%, var(--band) 100%);
    border-bottom: 3px solid var(--gold);
  }
  .label__panel {
    flex: 1;
    background: var(--panel);
    display: flex;
    flex-direction: column;
    align-items: center;
    padding-top: 22px;
  }
  .brand {
    display: flex;
    flex-direction: column;
    align-items: center;
    gap: 8px;
  }
  .brand__square {
    width: 40px; height: 40px;
    background: linear-gradient(135deg, var(--gold-light), var(--gold));
  }
  .brand__name {
    font-family: "Montserrat", sans-serif;
    font-weight: 500;
    font-size: 12px;
    letter-spacing: 1.5px;
    color: var(--gold);
  }
  .product-name {
    margin-top: 22px;
    font-size: 24px;
    line-height: 1;
    color: var(--ink);
  }
  .label--deep .product-name  { font-family: "Marcellus", serif; text-transform: uppercase; letter-spacing: 1px; }
  .label--mist .product-name  { font-family: "Italiana", serif; font-size: 29px; letter-spacing: .5px; }
  .label--blush .product-name { font-family: "Josefin Sans", sans-serif; font-weight: 300; text-transform: uppercase; letter-spacing: 1px; }
  .divider {
    width: 54px; height: 3px;
    margin-top: 18px;
    background: var(--gold);
  }
  .descriptor { margin-top: 22px; text-align: center; }
  .descriptor__en { font-size: 8.5px; letter-spacing: .6px; color: var(--ink); }
  .descriptor__fr { font-size: 8px; letter-spacing: .6px; color: var(--sub); margin-top: 3px; }
  .volume { margin-top: 18px; font-size: 6.5px; letter-spacing: .4px; color: var(--ink); }
  .certifications { margin-top: 16px; display: flex; gap: 22px; }
  .certification-badge { width: 17px; height: 17px; }
</style>
</head>
<body>

  <section class="label label--deep">
    <div class="label__leaf-band" role="img" aria-label="Gold leaf-vein pattern band"></div>
    <div class="label__panel">
      <div class="brand"><span class="brand__square"></span><span class="brand__name">LUMEN Ada</span></div>
      <h1 class="product-name">Velvet Harbor</h1>
      <span class="divider"></span>
      <div class="descriptor">
        <p class="descriptor__en">UNSCENTED HAIR CONDITIONER</p>
        <p class="descriptor__fr">APRÈS-SHAMPOING NON PARFUMÉ</p>
      </div>
      <p class="volume">238 ml ℮ 8 Fl. Oz.</p>
      <div class="certifications">
        <svg class="certification-badge" viewBox="0 0 20 20" role="img" aria-label="TQB certification"><circle cx="10" cy="10" r="8.5" fill="none" stroke="#f1ede4" stroke-width="1.5"/></svg>
        <svg class="certification-badge" viewBox="0 0 20 20" role="img" aria-label="Norvamark certification"><circle cx="10" cy="10" r="9.5" fill="#4aa3a5"/></svg>
        <svg class="certification-badge" viewBox="0 0 20 20" role="img" aria-label="Silver Kestrel certification"><circle cx="10" cy="10" r="8.5" fill="none" stroke="#f1ede4" stroke-width="1.5"/></svg>
      </div>
    </div>
  </section>

  <section class="label label--mist">
    <div class="label__leaf-band" role="img" aria-label="Gold leaf-vein pattern band"></div>
    <div class="label__panel">
      <div class="brand"><span class="brand__square"></span><span class="brand__name">LUMEN Ada</span></div>
      <h1 class="product-name">Velvet Harbor</h1>
      <span class="divider"></span>
      <div class="descriptor">
        <p class="descriptor__en">UNSCENTED HAIR CONDITIONER</p>
        <p class="descriptor__fr">APRÈS-SHAMPOING NON PARFUMÉ</p>
      </div>
      <p class="volume">238 ml ℮ 8 Fl. Oz.</p>
      <div class="certifications">
        <svg class="certification-badge" viewBox="0 0 20 20" role="img" aria-label="TQB certification"><circle cx="10" cy="10" r="8.5" fill="none" stroke="#3e5e6a" stroke-width="1.5"/></svg>
        <svg class="certification-badge" viewBox="0 0 20 20" role="img" aria-label="Norvamark certification"><circle cx="10" cy="10" r="9.5" fill="#4aa3a5"/></svg>
        <svg class="certification-badge" viewBox="0 0 20 20" role="img" aria-label="Silver Kestrel certification"><circle cx="10" cy="10" r="8.5" fill="none" stroke="#3e5e6a" stroke-width="1.5"/></svg>
      </div>
    </div>
  </section>

  <section class="label label--blush">
    <div class="label__leaf-band" role="img" aria-label="Gold leaf-vein pattern band"></div>
    <div class="label__panel">
      <div class="brand"><span class="brand__square"></span><span class="brand__name">LUMEN Ada</span></div>
      <h1 class="product-name">Velvet Harbor</h1>
      <span class="divider"></span>
      <div class="descriptor">
        <p class="descriptor__en">UNSCENTED HAIR CONDITIONER</p>
        <p class="descriptor__fr">APRÈS-SHAMPOING NON PARFUMÉ</p>
      </div>
      <p class="volume">238 ml ℮ 8 Fl. Oz.</p>
      <div class="certifications">
        <svg class="certification-badge" viewBox="0 0 20 20" role="img" aria-label="TQB certification"><circle cx="10" cy="10" r="8.5" fill="none" stroke="#6e5f60" stroke-width="1.5"/></svg>
        <svg class="certification-badge" viewBox="0 0 20 20" role="img" aria-label="Norvamark certification"><circle cx="10" cy="10" r="9.5" fill="#4aa3a5"/></svg>
        <svg class="certification-badge" viewBox="0 0 20 20" role="img" aria-label="Silver Kestrel certification"><circle cx="10" cy="10" r="8.5" fill="none" stroke="#6e5f60" stroke-width="1.5"/></svg>
      </div>
    </div>
  </section>

</body>
</html>
```